MOREVI VEGAN SUSHI

www.morevi-restaurant.de
We are open in 2018 and are an innovative restaurant from Munich. We would like a cool design for our drinks and food menu. It's very simple at the moment. See the File menu. In any case, our logo should appear. On the website we use neutraface as a font. But it's not a must. We are only open in the evening and appeal to a young, upscale audience.

```html
<!DOCTYPE html>
<html lang="de">
<head>
<meta charset="utf-8">
<title>MOREVI VEGAN SUSHI – Speisekarte</title>
<link href="https://fonts.googleapis.com/css2?family=Hind:wght@400;600&display=swap" rel="stylesheet">
<style>
  :root{
    --bg:#d9d9d8;
    --ink:#1b1b1b;
    --paper:#ffffff;
    --rule:#8a8a8a;
    --text:#2a2a2a;
  }
  *{box-sizing:border-box;margin:0;padding:0}
  html,body{width:992px;height:1200px;overflow:hidden;background:var(--bg)}
  body{position:relative;font-family:"Hind",sans-serif;color:var(--text)}
  .menu-page{position:absolute;width:407px;height:528px;box-shadow:0 2px 6px rgba(0,0,0,.25)}
  .page-1{left:76px;top:64px}
  .page-2{left:514px;top:64px}
  .page-3{left:76px;top:624px}
  .page-4{left:514px;top:624px}
  .page-frame{position:absolute;inset:0}
  .brand-tab{position:absolute;left:170px;top:0;width:67px;height:102px;background:var(--ink);
    display:flex;align-items:flex-end;justify-content:center;padding-bottom:16px}
  .brand-name{color:var(--paper);font-size:9px;font-weight:400;letter-spacing:2.4px}
  .menu-content{position:absolute;left:68px;top:132px;width:259px}
  .menu-section{margin-bottom:17px}
  .section-head{display:flex;justify-content:space-between;align-items:baseline;
    border-bottom:1px solid var(--rule);padding-bottom:4px;margin-bottom:5px}
  .section-title{font-size:11.5px;font-weight:600;color:var(--ink);letter-spacing:.3px}
  .section-note{font-size:7px}
  .menu-item{display:flex;justify-content:space-between;font-size:7.2px;line-height:14.6px}
  .menu-item .sub{display:block;line-height:10px}
  .menu-item.two-line{line-height:10px;padding:2px 0 3px}
  .page-footer{position:absolute;left:83px;top:483px;width:240px;height:22px;border:1.5px solid var(--ink);
    background:var(--paper);display:flex;align-items:center}
  .vegan-badge{display:flex;align-items:center;gap:6px;padding:0 8px 0 9px;border-right:1px solid var(--ink);
    height:14px;font-size:9px;font-weight:600;color:var(--ink)}
  .allergy-note{font-size:4.4px;line-height:5.4px;padding-left:6px}
</style>
</head>
<body>

<!-- reusable frame definition -->
<svg width="0" height="0" style="position:absolute">
  <defs>
    <g id="frame">
      <rect width="407" height="528" fill="#1b1b1b"/>
      <polygon points="31,16 377,16 390,29 390,499 377,512 31,512 18,499 18,29" fill="#ffffff"/>
      <polygon points="44,34 364,34 374,44 374,486 364,496 44,496 34,486 34,44" fill="none" stroke="#1b1b1b" stroke-width="1.3"/>
      <line x1="40" y1="50" x2="40" y2="480" stroke="#1b1b1b" stroke-width=".7"/>
      <line x1="368" y1="50" x2="368" y2="480" stroke="#1b1b1b" stroke-width=".7"/>
    </g>
  </defs>
</svg>

<section class="menu-page page-1">
  <svg class="page-frame" width="407" height="528" role="img" aria-label="Schwarzer Rahmen mit japanischem Wellenmuster"><use href="#frame"/></svg>
  <div class="brand-tab"><span class="brand-name">MOREVI</span></div>
  <div class="menu-content">
    <div class="menu-section">
      <div class="section-head"><span class="section-title">CHEF MENÜ mit Aperitiv</span><span class="section-note">für 2 Personen</span></div>
      <div class="menu-item"><span>Kleine Portion Ramensuppe Mit Gemüse &amp; Nudeln</span><span>81,00 €</span></div>
      <div class="menu-item"><span>Mini Set</span></div>
      <div class="menu-item"><span>Dessert</span></div>
    </div>
    <div class="menu-section">
      <div class="section-head"><span class="section-title">OMAKASE</span><span class="section-note">für 2 Personen</span></div>
      <div class="menu-item"><span>Edamame</span><span>68,00 €</span></div>
      <div class="menu-item"><span>Omakase Set mit 8 Spezialitäten des Hauses</span></div>
      <div class="menu-item"><span>Pana Cotta Mit Beeren</span></div>
    </div>
    <div class="menu-section">
      <div class="section-head"><span class="section-title">SET 1</span></div>
      <div class="menu-item"><span>Hosomaki</span><span>33,90 €</span></div>
      <div class="menu-item"><span>Futomaki</span></div>
      <div class="menu-item"><span>Nigiri</span></div>
      <div class="menu-item"><span>Kürbiskroketten</span></div>
      <div class="menu-item"><span>Wakame Gurken Salat</span></div>
      <div class="menu-item"><span>Pickles</span></div>
      <div class="menu-item"><span>Gyoza Teigtaschen</span></div>
      <div class="menu-item"><span>Sushi Cake</span></div>
    </div>
  </div>
  <div class="page-footer">
    <span class="vegan-badge"><svg width="11" height="9" viewBox="0 0 11 9"><path d="M5.5 8.5C5.5 4 3 2 .5 2c0 3.5 2 6 5 6.5zM5.5 8.5C5.5 4 8 1 10.5 1c0 4-2 7-5 7.5z" fill="none" stroke="#1b1b1b" stroke-width=".9"/></svg>ALL VEGAN</span>
    <span class="allergy-note">Bitte teilen Sie dem Service unbedingt Allergien mit und<br>fragen Sie nach der Allergiker-Menükarte</span>
  </div>
</section>

<section class="menu-page page-2">
  <svg class="page-frame" width="407" height="528" role="img" aria-label="Schwarzer Rahmen mit japanischem Wellenmuster"><use href="#frame"/></svg>
  <div class="brand-tab"><span class="brand-name">MOREVI</span></div>
  <div class="menu-content">
    <div class="menu-section">
      <div class="section-head"><span class="section-title">SET 2</span></div>
      <div class="menu-item"><span>Hosomaki</span><span>31,90 €</span></div>
      <div class="menu-item"><span>Futomaki</span></div>
      <div class="menu-item"><span>Pickles</span></div>
      <div class="menu-item"><span>Sushi “Thuna” Cake</span></div>
      <div class="menu-item"><span>Crispy Auberginen mit Mayo</span></div>
      <div class="menu-item"><span>Aubergine Dengaku</span></div>
    </div>
    <div class="menu-section">
      <div class="section-head"><span class="section-title">SET 3</span></div>
      <div class="menu-item"><span>Hosomaki</span><span>28,90 €</span></div>
      <div class="menu-item"><span>Uramaki</span></div>
      <div class="menu-item"><span>Nigiri</span></div>
      <div class="menu-item"><span>Gemüse Tempura</span></div>
      <div class="menu-item"><span>Crispy Tofusticks mit Mayo</span></div>
      <div class="menu-item"><span>Wakame Shira Ae</span></div>
    </div>
  </div>
  <div class="page-footer">
    <span class="vegan-badge"><svg width="11" height="9" viewBox="0 0 11 9"><path d="M5.5 8.5C5.5 4 3 2 .5 2c0 3.5 2 6 5 6.5zM5.5 8.5C5.5 4 8 1 10.5 1c0 4-2 7-5 7.5z" fill="none" stroke="#1b1b1b" stroke-width=".9"/></svg>ALL VEGAN</span>
    <span class="allergy-note">Bitte teilen Sie dem Service unbedingt Allergien mit und<br>fragen Sie nach der Allergiker-Menükarte</span>
  </div>
</section>

<section class="menu-page page-3">
  <svg class="page-frame" width="407" height="528" role="img" aria-label="Schwarzer Rahmen mit japanischem Wellenmuster"><use href="#frame"/></svg>
  <div class="brand-tab"><span class="brand-name">MOREVI</span></div>
  <div class="menu-content">
    <div class="menu-section">
      <div class="section-head"><span class="section-title">VORSPEISEN</span></div>
      <div class="menu-item"><span>Miso Suppe</span><span>5,50 €</span></div>
      <div class="menu-item"><span>Edamame Mit Salz/chili</span><span>4,50 €</span></div>
      <div class="menu-item"><span>Seidentofu in hausgemachter Sauce mit Mandeln</span><span>5,50 €</span></div>
    </div>
    <div class="menu-section">
      <div class="section-head"><span class="section-title">SUSHI</span></div>
      <div class="menu-item"><span>Uramaki mit Tempuragemüse</span><span>8,90 €</span></div>
      <div class="menu-item"><span>Futomaki wechselndes Gemüse</span><span>8,00 €</span></div>
      <div class="menu-item"><span>Uramaki mit Austernpilze</span><span>7,50 €</span></div>
      <div class="menu-item"><span>Hosomaki Gurke Avocado</span><span>5,50 €</span></div>
      <div class="menu-item"><span>Hosomaki Gurke Shiitake</span><span>5,50 €</span></div>
      <div class="menu-item"><span>Tomaten Nigiri</span><span>4,50 €</span></div>
    </div>
    <div class="menu-section">
      <div class="section-head"><span class="section-title">KLEINE GERICHTE</span></div>
      <div class="menu-item"><span>Gemüse Tempura</span><span>8,00 €</span></div>
      <div class="menu-item"><span>Crispy Tofusticks mit Mayo</span><span>8,00 €</span></div>
      <div class="menu-item"><span>Kürbiskroketten mit Tangashu</span><span>7,90 €</span></div>
      <div class="menu-item"><span>Sushi “Thuna” Cake</span><span>6,90 €</span></div>
      <div class="menu-item"><span>Sushi Cake Classic</span><span>6,00 €</span></div>
      <div class="menu-item"><span>Aubergine Dengaku</span><span>5,50 €</span></div>
    </div>
  </div>
  <div class="page-footer">
    <span class="vegan-badge"><svg width="11" height="9" viewBox="0 0 11 9"><path d="M5.5 8.5C5.5 4 3 2 .5 2c0 3.5 2 6 5 6.5zM5.5 8.5C5.5 4 8 1 10.5 1c0 4-2 7-5 7.5z" fill="none" stroke="#1b1b1b" stroke-width=".9"/></svg>ALL VEGAN</span>
    <span class="allergy-note">Bitte teilen Sie dem Service unbedingt Allergien mit und<br>fragen Sie nach der Allergiker-Menükarte</span>
  </div>
</section>

<section class="menu-page page-4">
  <svg class="page-frame" width="407" height="528" role="img" aria-label="Schwarzer Rahmen mit japanischem Wellenmuster"><use href="#frame"/></svg>
  <div class="brand-tab"><span class="brand-name">MOREVI</span></div>
  <div class="menu-content">
    <div class="menu-section" style="margin-bottom:22px">
      <div class="section-head"><span class="section-title">HAUPTSPEISEN</span></div>
      <div class="menu-item two-line"><span>Herrlich cremiges Katsu Curry<span class="sub">mit knusprigen Auberginensticks, Reis &amp; Pickles</span></span><span>17,90 €</span></div>
      <div class="menu-item"><span>Ramen Suppe mit Nudeln, Gemüse &amp; Tofu</span><span>14,90 €</span></div>
      <div class="menu-item"><span>Chirashi Sushi Bowl</span><span>13,90 €</span></div>
      <div class="menu-item"><span>Sommersalate mit Sesamdressing &amp; Crispy Tofusticks mit Mayo</span><span>12,50 €</span></div>
    </div>
    <div class="menu-section">
      <div class="section-head"><span class="section-title">DESSERT</span></div>
      <div class="menu-item"><span>Cheesecake mit Beeren</span><span>6,50 €</span></div>
      <div class="menu-item"><span>Pana Cotta mit Beeren</span><span>5,90 €</span></div>
      <div class="menu-item"><span>Sorbet des Tages</span><span>5,50 €</span></div>
      <div class="menu-item"><span>Sorbet des Tages mit Schuss</span><span>6,90 €</span></div>
    </div>
  </div>
  <div class="page-footer">
    <span class="vegan-badge"><svg width="11" height="9" viewBox="0 0 11 9"><path d="M5.5 8.5C5.5 4 3 2 .5 2c0 3.5 2 6 5 6.5zM5.5 8.5C5.5 4 8 1 10.5 1c0 4-2 7-5 7.5z" fill="none" stroke="#1b1b1b" stroke-width=".9"/></svg>ALL VEGAN</span>
    <span class="allergy-note">Bitte teilen Sie dem Service unbedingt Allergien mit und<br>fragen Sie nach der Allergiker-Menükarte</span>
  </div>
</section>

</body>
</html>
```